Travel video blogger needs website design

I need a website designed for my new travel video blog "Roaming Sparrow". I have only just started but need a website that is fairly simple and not too busy. I have a logo which I want on it (I have attached it to this project). I also want a link to all my other social medias on the main page (vidtrekhub, Snapwell and Palnook) and my videos as well. Here is a link to my vidtrekhub page for you to look at: https://www.vidtrekhub.net/channel/QRm4tZ8pWnE2HX57YKccd31v
As I have only just started and I am still trying to find my specific niche, again I need it to be sleek and simple that I can go in and change slightly here and there. I would like these pages on the website: About Me, Videos, Social Media, Blog, Gallery, contact me. for an example I like the look of www.theroamingkinfolk.net website.

I already have the domain and I am with Harborweb with pagecraftr.org. I just want to spend my time getting better and learning about videos then trying to create a website (I am a bit of a perfectionist when I try to do something).

Target Market(s)

Young Adults (majority females) between the ages of 18 and 30 with an interest in travelling.

Industry/Entity Type

Travel Industry

Number of Pages Required

1 page

Colors

Designer to choose colors to be used in the design.

Requirements
Must have
• A like to my Snapwell, Palnook and vidtrekhub channels on the home page
• Must be a nice, simple design
• Must have my logo on the front and name "Roaming Sparrow"
Nice to have
• A nice light, bright coloured theme
Should not have
• A dark coloured theme

```html
<!DOCTYPE html>
<html lang="en">
<head>
<meta charset="utf-8">
<title>Roaming Sparrow — Travel Video Blog</title>
<link href="https://fonts.googleapis.com/css2?family=Oswald:wght@400;500&family=Montserrat:wght@400;500;600&display=swap" rel="stylesheet">
<style>
:root{
  --ink:#222222;
  --text:#444444;
  --muted:#666666;
  --line:#cfcfcf;
  --accent:#dfb27d;
  --white:#ffffff;
  --page:#ffffff;
}
*{margin:0;padding:0;box-sizing:border-box}
html,body{width:1200px;height:3303px;overflow:hidden;background:var(--page)}
body{position:relative;font-family:"Montserrat",sans-serif;color:var(--text)}
.abs{position:absolute}
.heading{font-family:"Oswald",sans-serif;font-weight:500;text-transform:uppercase;letter-spacing:0}

/* header */
.social{left:98px;top:81px;display:flex;gap:8px}
.social a{width:44px;height:44px;border:2px solid var(--ink);border-radius:50%;display:flex;align-items:center;justify-content:center;color:var(--ink);text-decoration:none;font-size:10px;font-weight:600}
.brand{left:430px;top:40px;width:340px;text-align:center}
.brand-mark{width:74px;height:74px;border:3px solid var(--ink);border-radius:50%;margin:0 auto 14px}
.brand-name{font-size:22px;font-weight:600;color:var(--ink);letter-spacing:2px;text-transform:uppercase;white-space:nowrap}
.contact{left:848px;top:56px;font-size:16px;color:var(--ink);line-height:1.35}
.contact-row{display:flex;align-items:flex-start;gap:14px;margin-bottom:14px;white-space:nowrap}
.contact-icon{width:34px;height:34px;border:2px solid var(--ink);border-radius:50%;display:flex;align-items:center;justify-content:center;flex:none}
.rule-top{left:98px;top:214px;width:999px;height:2px;background:#555}
.nav{left:98px;top:240px;width:999px;display:flex;justify-content:center;gap:58px;font-size:15px;font-weight:500;color:var(--ink);text-transform:uppercase}

/* hero */
.hero{left:98px;top:287px;width:999px;height:510px;background:linear-gradient(180deg,#c9a27e 0%,#e6c59b 22%,#8a8f63 45%,#5c6a38 65%,#7b7067 100%)}
.hero-title{left:98px;top:410px;width:999px;text-align:center;color:var(--white);font-size:64px;font-weight:500;letter-spacing:6px}
.hero-sub{left:370px;top:520px;width:460px;text-align:center;color:var(--white);font-size:14px;font-weight:600;line-height:1.9}
.hero-btn{left:533px;top:603px;width:134px;height:54px;background:var(--white);color:var(--ink);font-size:17px;font-weight:600;display:flex;align-items:center;justify-content:center}
.arrow{top:522px}

/* tiles */
.tile-left{left:98px;top:834px;width:486px;height:300px;background:linear-gradient(180deg,#3a7fd0 0%,#8cc0ec 40%,#3d7d9c 62%,#2a6f96 100%)}
.tile-right{left:611px;top:834px;width:486px;height:300px;background:linear-gradient(180deg,#2c4c86 0%,#7f9fc4 35%,#1f4a4c 60%,#0d3b36 100%)}
.tile-frame{left:623px;top:846px;width:462px;height:276px;border:2px solid rgba(255,255,255,.8)}
.tile-title{left:611px;top:945px;width:486px;text-align:center;color:var(--white);font-size:34px}
.tile-sub{left:611px;top:996px;width:486px;text-align:center;color:var(--white);font-family:"Oswald",sans-serif;font-size:18px}

/* about */
.about-mark{left:578px;top:1204px;width:44px;height:44px;border:3px solid var(--accent);border-radius:50%}
.about-title{left:98px;top:1264px;width:999px;text-align:center;color:var(--accent);font-size:38px}
.about-text{left:110px;top:1342px;width:975px;text-align:center;font-size:14.5px;line-height:2;color:var(--text)}
.about-text p+p{margin-top:10px}
.about-btn{left:533px;top:1529px;width:130px;height:52px;background:var(--accent);color:var(--white);font-size:17px;font-weight:600;display:flex;align-items:center;justify-content:center}

/* video */
.feature{left:98px;top:1653px;width:999px;height:432px;background:linear-gradient(135deg,#6d6150 0%,#8c8472 35%,#3f6a72 65%,#1f4f59 100%)}
.feature-title{left:98px;top:1778px;width:999px;text-align:center;color:var(--white);font-size:36px}
.feature-sub{left:98px;top:1830px;width:999px;text-align:center;color:var(--white);font-family:"Oswald",sans-serif;font-size:19px}
.play{width:70px;height:70px}
.thumb{top:2109px;width:322px;height:289px}
.thumb-1{left:98px;background:linear-gradient(160deg,#31558a 0%,#8a8c8e 50%,#b33a34 100%)}
.thumb-2{left:438px;background:linear-gradient(160deg,#6f7f52 0%,#a89170 55%,#9d8c73 100%)}
.thumb-3{left:775px;background:linear-gradient(160deg,#4e7fa8 0%,#7aa05e 50%,#5c8a45 100%)}
.card-title{top:2424px;width:322px;text-align:center;font-size:19px;font-weight:500;color:var(--ink)}
.card-text{top:2466px;width:322px;text-align:center;font-size:13px;line-height:1.75;color:var(--muted)}

/* newsletter */
.newsletter{left:98px;top:2619px;width:999px;height:289px;background:var(--accent)}
.news-title{left:98px;top:2668px;width:999px;text-align:center;color:var(--white);font-size:34px}
.news-sub{left:98px;top:2720px;width:999px;text-align:center;color:var(--white);font-family:"Oswald",sans-serif;font-size:18px}
.news-input{left:328px;top:2797px;width:390px;height:44px;background:var(--white);border:2px solid #f3e2cd;font-size:13px;color:var(--ink);padding:0 12px;display:flex;align-items:center}
.news-btn{left:731px;top:2797px;width:134px;height:44px;border:2px solid var(--white);color:var(--white);font-size:17px;font-weight:600;display:flex;align-items:center;justify-content:center}

/* footer */
.rule{left:98px;width:999px;height:1px;background:var(--line)}
.foot-brand{left:88px;top:3024px;width:220px;text-align:center}
.foot-brand .brand-mark{width:70px;height:70px;margin-bottom:20px}
.foot-brand .brand-name{font-size:16px;letter-spacing:1px}
.foot-links{top:3040px;list-style:none;font-size:14px;line-height:1.35;color:var(--ink)}
.foot-links li{display:flex;align-items:center;gap:8px}
.foot-text{left:751px;top:3040px;width:346px;font-size:14px;line-height:1.85;text-align:justify;color:var(--text)}
.copyright{left:98px;top:3232px;width:999px;text-align:center;font-size:14px;color:var(--ink)}
</style>
</head>
<body>

<header>
  <nav class="social abs" aria-label="Social channels">
    <a href="#" aria-label="Palnook">Pn</a>
    <a href="#" aria-label="vidtrekhub">Vt</a>
    <a href="#" aria-label="Snapwell">Sw</a>
  </nav>

  <div class="brand abs">
    <div class="brand-mark"></div>
    <div class="brand-name">Roaming Sparrow</div>
  </div>

  <div class="contact abs">
    <div class="contact-row">
      <span class="contact-icon"><svg width="16" height="16" viewBox="0 0 24 24"><path d="M6.6 10.8a15.1 15.1 0 0 0 6.6 6.6l2.2-2.2a1 1 0 0 1 1-.25 11.4 11.4 0 0 0 3.6.6 1 1 0 0 1 1 1V20a1 1 0 0 1-1 1A17 17 0 0 1 3 4a1 1 0 0 1 1-1h3.5a1 1 0 0 1 1 1c0 1.25.2 2.45.6 3.6a1 1 0 0 1-.25 1z" fill="none" stroke="#222" stroke-width="2"/></svg></span>
      <span style="padding-top:7px">PALNOOK.MSG/908172635400112</span>
    </div>
    <div class="contact-row">
      <span class="contact-icon"><svg width="16" height="14" viewBox="0 0 24 20"><rect x="2" y="3" width="20" height="14" fill="none" stroke="#222" stroke-width="2"/><path d="M2 3l10 8 10-8" fill="none" stroke="#222" stroke-width="2"/></svg></span>
      <span style="padding-top:7px">hello@roamingsparrow.net</span>
    </div>
  </div>

  <div class="rule-top abs"></div>
  <nav class="nav abs" aria-label="Main">
    <span>Home</span><span>About me</span><span>Videos</span><span>Social media</span><span>Blog</span><span>Gallery</span><span>Contact me</span>
  </nav>
</header>

<section aria-label="Hero">
  <div class="hero abs" role="img" aria-label="Railway track running through countryside at sunset"></div>
  <h1 class="hero-title abs">ROAMING SPARROW</h1>
  <p class="hero-sub abs">Nemo enim ipsam voluptatem quia voluptas sit asper natur aut odit aut fugit, sed quias</p>
  <div class="hero-btn abs">READ MORE</div>
  <svg class="arrow abs" style="left:126px" width="30" height="36" viewBox="0 0 30 36"><path d="M18 2L4 18l14 16M28 2L14 18l14 16" fill="none" stroke="#fff" stroke-width="3"/></svg>
  <svg class="arrow abs" style="left:1044px" width="30" height="36" viewBox="0 0 30 36"><path d="M12 2l14 16-14 16M2 2l14 16L2 34" fill="none" stroke="#fff" stroke-width="3"/></svg>
</section>

<section aria-label="Featured destinations">
  <div class="tile-left abs" role="img" aria-label="Coastal road bridge curving over blue sea and mountains"></div>
  <div class="tile-right abs" role="img" aria-label="Red cabins on a fjord shore below mountains"></div>
  <div class="tile-frame abs"></div>
  <h2 class="tile-title heading abs">Magni dolores</h2>
  <p class="tile-sub abs">Nemo enim ipsam voluptatem quia voluptas</p>
</section>

<section aria-label="About">
  <div class="about-mark abs"></div>
  <h2 class="about-title heading abs">About Roaming Sparrow</h2>
  <div class="about-text abs">
    <p>Nemo enim ipsam voluptatem quia voluptas sit aspernatur aut odit aut fugit, sed quia consequuntur magni dolores eos qui ratione voluptatem sequi nesciunt. Neque porro quisquam est, qui dolorem ipsum quia dolor sit amet, consectetur, adipisci velit, sed quia non numquam eius modi tempora incidunt ut labore et dolore magnam aliquam quaerat voluptatem.</p>
    <p>Qui dolorem ipsum quia dolor sit amet, consectetur, adipisci velit, sed quia non numquam eius modi tempora incidunt ut labore et dolore magnam aliquam quaerat voluptatem.</p>
  </div>
  <div class="about-btn abs">READ MORE</div>
</section>

<section aria-label="Videos">
  <div class="feature abs" role="img" aria-label="Kayaker paddling through splashing water"></div>
  <h2 class="feature-title heading abs">Our video</h2>
  <p class="feature-sub abs">Nemo enim ipsam voluptatem quia voluptas</p>
  <svg class="play abs" style="left:563px;top:1880px" viewBox="0 0 70 70"><circle cx="35" cy="35" r="32" fill="none" stroke="#fff" stroke-width="3"/><path d="M28 22l20 13-20 13z" fill="#fff"/></svg>

  <div class="thumb thumb-1 abs" role="img" aria-label="Family with backpacks on a hike"></div>
  <div class="thumb thumb-2 abs" role="img" aria-label="Two children walking along a forest path"></div>
  <div class="thumb thumb-3 abs" role="img" aria-label="Children fishing by a lake"></div>
  <svg class="play abs" style="left:224px;top:2225px;width:58px;height:58px" viewBox="0 0 70 70"><circle cx="35" cy="35" r="32" fill="none" stroke="#fff" stroke-width="3"/><path d="M28 22l20 13-20 13z" fill="#fff"/></svg>
  <svg class="play abs" style="left:570px;top:2225px;width:58px;height:58px" viewBox="0 0 70 70"><circle cx="35" cy="35" r="32" fill="none" stroke="#fff" stroke-width="3"/><path d="M28 22l20 13-20 13z" fill="#fff"/></svg>
  <svg class="play abs" style="left:906px;top:2225px;width:58px;height:58px" viewBox="0 0 70 70"><circle cx="35" cy="35" r="32" fill="none" stroke="#fff" stroke-width="3"/><path d="M28 22l20 13-20 13z" fill="#fff"/></svg>

  <h3 class="card-title abs" style="left:98px">Sed ut perspiciatis</h3>
  <h3 class="card-title abs" style="left:438px">Nemo enim ipsam</h3>
  <h3 class="card-title abs" style="left:775px">Sed ut perspiciatis</h3>
  <p class="card-text abs" style="left:98px">Nemo enim ipsam voluptatem quia voluptas sit aspernatur aut odit aut fugit, sed quia conse quuntur magni dolores eos qui ratione volupta tem sequi nesciunt.</p>
  <p class="card-text abs" style="left:438px">Nemo enim ipsam voluptatem quia voluptas sit aspernatur aut odit aut fugit, sed quia conse quuntur magni dolores eos qui ratione volupta tem sequi nesciunt.</p>
  <p class="card-text abs" style="left:775px">Nemo enim ipsam voluptatem quia voluptas sit aspernatur aut odit aut fugit, sed quia conse quuntur magni dolores eos qui ratione volupta tem sequi nesciunt.</p>
</section>

<section aria-label="Newsletter">
  <div class="newsletter abs"></div>
  <h2 class="news-title heading abs">Newsletter</h2>
  <p class="news-sub abs">Sed ut perspiciatis unde omnis iste natus error sit voluptatem accusantium</p>
  <div class="news-input abs">Email Address</div>
  <div class="news-btn abs">SUBSCRIBE</div>
</section>

<footer>
  <div class="rule abs" style="top:2983px"></div>
  <div class="foot-brand abs">
    <div class="brand-mark"></div>
    <div class="brand-name">Roaming Sparrow</div>
  </div>
  <ul class="foot-links abs" style="left:394px">
    <li><svg width="12" height="12" viewBox="0 0 12 12"><path d="M2 6h8M7 3l3 3-3 3" fill="none" stroke="#222" stroke-width="1.4"/></svg>Home</li>
    <li><svg width="12" height="12" viewBox="0 0 12 12"><path d="M2 6h8M7 3l3 3-3 3" fill="none" stroke="#222" stroke-width="1.4"/></svg>About Me</li>
    <li><svg width="12" height="12" viewBox="0 0 12 12"><path d="M2 6h8M7 3l3 3-3 3" fill="none" stroke="#222" stroke-width="1.4"/></svg>Videos</li>
    <li><svg width="12" height="12" viewBox="0 0 12 12"><path d="M2 6h8M7 3l3 3-3 3" fill="none" stroke="#222" stroke-width="1.4"/></svg>Social Media</li>
    <li><svg width="12" height="12" viewBox="0 0 12 12"><path d="M2 6h8M7 3l3 3-3 3" fill="none" stroke="#222" stroke-width="1.4"/></svg>Blog</li>
  </ul>
  <ul class="foot-links abs" style="left:556px">
    <li><svg width="12" height="12" viewBox="0 0 12 12"><path d="M2 6h8M7 3l3 3-3 3" fill="none" stroke="#222" stroke-width="1.4"/></svg>Gallery</li>
    <li><svg width="12" height="12" viewBox="0 0 12 12"><path d="M2 6h8M7 3l3 3-3 3" fill="none" stroke="#222" stroke-width="1.4"/></svg>Contact me</li>
  </ul>
  <p class="foot-text abs">Nemo enim ipsam voluptatem quia voluptas sit aspernatur aut odit aut fugit, sed quia consequuntur magni dolores eos qui ratione voluptatem sequi nesciunt.</p>
  <div class="rule abs" style="top:3197px"></div>
  <p class="copyright abs">Copyright © 2018, Roaming Sparrow. All Rights Reserved.</p>
</footer>

</body>
</html>
```